Need a small Brochure Designing for a High Tech LED Spotlight

This is an expensive product and the best of it's kind in the world, so it needs to be marketed to intelligent, forward thinking people who appreciate and pay for excellent design and innovation. The type of people who buy Quince products i guess. It needs to be clean. The colours do not need to be in keep with our website, but our logo does need to be on the brochure. I have attached a dcoument with all the text, the order the text goes in and an idea of how i want the first page to look. All images and logos have been attached too.

Target Market(s)

This is aimed at people with high disposible incomes who spend money on the best designed products and the latest technology. The type of people who buy Quince products.

Industry/Entity Type

Product

Requirements
Must have
• The work needs to be editable by us using indesign

The pages need to be A5. I'm not sure how many pages the brochure needs to be as it does need to be clean and be spaced out well. On the file that contains the text i've indicated that 8 pages would be good.

The logos i attached - 1) Kelo Product Design Award, 2) Z Technology Award, 3) Blue Fern Design Award and 4) Keen Design Award all need to be at the bottom of the front page, quite small, but still able to see them well.

- Needs to have a QR code so that smart phones can scan the code and be taken to a pol vane clip - QR code is attached.
- Needs to have Plimbo Icon - @KestrowHomeCo
Nice to have
• Nice to remind customers on each page that the product has a 5 year Warranty and we have a 365 day Returns Policy.

```html
<!DOCTYPE html>
<html lang="en">
<head>
<meta charset="utf-8">
<title>K7 LED Spotlight Brochure – Spread</title>
<link href="https://fonts.googleapis.com/css2?family=Nunito:wght@700&family=Questrial&family=Quicksand:wght@300&display=swap" rel="stylesheet">
<style>
  :root{
    --canvas:#ffffff;
    --page:#ffffff;
    --quote-mark:#e2ebe2;
    --quote-text:#8cbf8a;
    --heading:#2c8a32;
    --body:#555555;
    --photo-dark:#6b6158;
    --photo-mid:#a39a90;
    --photo-light:#d8d2ca;
    --panel:rgba(240,238,234,0.85);
    --fragment:#6c6c6c;
  }
  html,body{margin:0;padding:0;width:1200px;height:900px;overflow:hidden;background:var(--canvas);}
  .canvas{position:relative;width:1200px;height:900px;overflow:hidden;}
  .facing-photo{
    position:absolute;left:0;top:88px;width:74px;height:708px;
    background:linear-gradient(180deg,#c9c2b8 0%,var(--photo-mid) 22%,#8a837c 35%,#4f4a45 45%,var(--photo-light) 46%,#e6e2dc 70%,#cfc6bb 85%,var(--photo-dark) 100%);
  }
  .facing-panel{position:absolute;left:0;top:410px;width:74px;height:342px;background:var(--panel);}
  .facing-fragment{
    position:absolute;left:0;width:15px;margin:0;overflow:visible;
    font-family:"Questrial",sans-serif;font-style:italic;font-size:13px;color:var(--fragment);
    line-height:17px;text-align:right;white-space:nowrap;direction:rtl;
  }
  .spread-page{
    position:absolute;left:74px;top:88px;width:1006px;height:708px;overflow:hidden;
    background:var(--page);box-shadow:0 1px 4px rgba(0,0,0,0.25);
  }
  .quote-marks{position:absolute;left:0;top:0;width:1006px;height:230px;}
  .quote-marks path{fill:var(--quote-mark);}
  .pull-quote{
    position:absolute;left:280px;top:110px;margin:0;
    font-family:"Quicksand",sans-serif;font-weight:300;font-style:italic;
    font-size:38px;line-height:46px;color:var(--quote-text);letter-spacing:0.3px;
  }
  .feature{position:absolute;top:340px;width:431px;}
  .feature--heat{left:61px;}
  .feature--brightness{left:515px;}
  .feature-title{
    margin:0 0 17px;font-family:"Nunito",sans-serif;font-weight:700;
    font-size:19px;line-height:26px;color:var(--heading);
  }
  .feature-text{
    margin:0 0 17px;font-family:"Questrial",sans-serif;font-size:13.6px;
    line-height:17.2px;color:var(--body);text-align:justify;
  }
</style>
</head>
<body>
<div class="canvas">
  <div class="facing-photo" role="img" aria-label="Photograph of a modern kitchen with oven and pale cabinetry lit by LED spotlights"></div>
  <div class="facing-panel"></div>
  <p class="facing-fragment" style="top:469px">ail.</p>
  <p class="facing-fragment" style="top:503px">us<br>rd,<br>ot</p>
  <p class="facing-fragment" style="top:589px">ve<br>ng<br>ED<br>at</p>
  <p class="facing-fragment" style="top:694px">gn</p>

  <section class="spread-page">
    <svg class="quote-marks" viewBox="0 0 1006 230" aria-hidden="true">
      <path d="M66 0 H132 L108 92 H130 L108 195 H0 L22 98 Z"/>
      <path d="M226 0 H292 L268 92 H290 L268 195 H160 L182 98 Z"/>
      <path d="M518 177 H535 L527 193 L516 209 H510 L516 193 H511 Z"/>
      <path d="M540 177 H557 L549 193 L538 209 H532 L538 193 H533 Z"/>
    </svg>
    <p class="pull-quote">Cut your energy consumption<br>by up to 90%</p>

    <article class="feature feature--heat">
      <h2 class="feature-title">Heat Dissipation</h2>
      <p class="feature-text">The brightness of all LEDs deteriorates over time. Just how quickly, though, is almost exclusively down to how well the lamp can dissipate heat.</p>
      <p class="feature-text">Heat is the biggest enemy of the LED. Without proper heat dissipation, the critical components of any LED lamp will fail or degrade quickly. So if the LED spotlight doesn’t have a well-designed, thorough heat dissipation system, the quality of light will easily degrade to an unacceptable level, with the LED simply failing very quickly.</p>
      <p class="feature-text">The K7 7w is crafted from the finest raw materials and uses a cutting edge heat dissipation system similar to that used to cool fuel tanks on Aerion space shuttles and brake callipers on Apex One cars.</p>
      <p class="feature-text">This beautiful, intuitive patented design has won multiple international awards.</p>
    </article>

    <article class="feature feature--brightness">
      <h2 class="feature-title">Brightness</h2>
      <p class="feature-text">Velar manufacture the most advanced and powerful LED chips in the world. While rival companies now produce very reasonable alternatives, there’s still no substitute for Velar.</p>
      <p class="feature-text">The K7 uses the very latest Velar VX-E Chip, which produces 580 warm white lumens. With 83 lumens per watt, the K7 is considerably more powerful than a 50w halogen – and any other LED spot.</p>
      <p class="feature-text">A Lumetra LS-60T integrating sphere (a rare and very expensive piece of equipment) is used to measure the total light radiated in all directions from the lamp, giving customers a 100% accurate measurement of its total power or “flux”.</p>
    </article>
  </section>
</div>
</body>
</html>
```